Product Page

We're marketing an on line educational product, and need a savvy designer to fix a web page that lacks pazazz. We're looking for a designer who can take a lot of information and present it neatly and elegantly, and put all the relevant testimonials in there without loosing cool factor. Right now we need just one page designed, but the winner will have the chance to re-do the entire site, with lots more content coming down the line that will need the new look.

The current page is here: www.plorvetune.com/sign-up. This should be combined with the attached PDF that has a lot more text information.

Note: The previous file listed as a pdf was a jpg. Sorry about that! Now there's a real pdf available for you to download.

I have added a jpg of myself. If you can use that I would appreciate it. I've also uploaded an example of a pricing page. Let me know how you would charge for this extra page.

Target Market(s)

Men and women in their forties who want to improve their singing but have other careers and are looking for high quality voice instruction.

The page must have an attractive "Get Started" button prominently displayed.

Industry/Entity Type

Marketing

Requirements
Must have
• Above the fold: clear buy now button, some testimonials, and the video. Should have a background that makes reading the text easy-not black. The new page must work somehow with the existing theme, although we will be re-designing the whole site soon with your help.
Nice to have
• Some navigation to organize a lot of text

```html
<!DOCTYPE html>
<html lang="en">
<head>
<meta charset="utf-8">
<title>Marlowe School of Voice – Voice Ascent</title>
<link rel="stylesheet" href="https://fonts.googleapis.com/css2?family=Open+Sans:wght@300;400;600;700&display=swap">
<style>
:root{
  --navy:#0f2535;
  --navy-deep:#0a1b27;
  --slate:#1d4a66;
  --accent:#2a9fd6;
  --accent-light:#45b4ea;
  --accent-dark:#1a7fb4;
  --ink:#333;
  --muted:#6b6b6b;
  --panel:#e8ecef;
  --white:#fff;
}
*{box-sizing:border-box;margin:0;padding:0}
html,body{width:1200px;height:2370px;overflow:hidden}
body{font-family:"Open Sans",Arial,sans-serif;color:var(--ink);background:var(--white);position:relative}
a{color:inherit;text-decoration:none}
.wrap{position:relative;width:820px;margin:0 auto}

/* Header */
.site-header{height:118px;background:var(--navy)}
.topbar{height:30px;display:flex;justify-content:space-between;align-items:center;font-size:11.5px;color:var(--accent-light);border-bottom:1px solid rgba(255,255,255,.12)}
.topbar strong{color:var(--white);font-weight:400}
.topbar .signin{color:var(--white);font-weight:600}
.mainbar{height:88px;display:flex;justify-content:space-between;align-items:center}
.brand{display:flex;align-items:center;gap:10px;color:var(--white);font-size:23px;font-weight:600}
.brand-mark{width:26px;height:26px;border:2px solid var(--accent-light);border-radius:50%}
.main-nav{display:flex;gap:19px;font-size:12.5px;font-weight:600;color:var(--white)}

/* Hero */
.hero{height:370px;position:relative;text-align:center;background:linear-gradient(100deg,#0d4a66 0%,#15759c 45%,#1c6f93 75%,#2a87ad 100%)}
.hero-title{padding-top:16px;font-size:29px;font-weight:400;color:var(--accent-light);line-height:34px}
.hero-sub{font-size:21px;color:var(--white);font-weight:400;line-height:30px}
.video-panel{position:absolute;left:191px;top:87px;width:820px;height:257px;background:rgba(8,28,42,.88);display:flex;text-align:left}
.video-frame{margin:13px 0 0 14px;width:382px;height:232px;border:8px solid #c9cdd0;background:linear-gradient(180deg,#1c1c1c,#3a3a3a);position:relative}
.video-caption{position:absolute;left:0;right:0;bottom:14px;text-align:center;font-size:11px;color:#9a9a9a}
.play{position:absolute;left:50%;top:50%;transform:translate(-50%,-60%)}
.video-copy{padding:10px 18px 0 18px;color:var(--white)}
.video-copy .lead{font-size:14.5px;line-height:21px}
.video-copy .body{margin-top:12px;font-size:11.2px;line-height:19px;color:#e5eef3;text-align:justify}
.cta-line{margin-top:14px;display:flex;align-items:center;gap:12px;font-size:12px;color:#e5eef3}
.btn{display:inline-flex;align-items:center;gap:6px;height:28px;padding:0 14px;font-size:12px;font-weight:600;border-radius:3px}
.btn-blue{background:var(--accent);color:var(--white);border:1px solid #55c0f0}
.btn-grey{background:#e4e4e4;color:#555;border:1px solid #cfcfcf}

/* About */
.about{height:434px;background:linear-gradient(180deg,#fff 0%,#fdfdfd 70%,#f3f3f3 100%)}
.about .wrap{padding-top:20px;display:flex;justify-content:space-between}
.about-text{width:540px}
.about h2{font-size:22px;font-weight:400;color:var(--ink);padding-bottom:12px;border-bottom:1px solid #e2e2e2;width:490px}
.about .lead{margin-top:10px;font-size:14.5px;line-height:24px;color:var(--accent)}
.about .body{margin-top:14px;font-size:11.3px;line-height:24px;color:var(--muted)}
.about .body + .body{margin-top:24px}
.about .actions{margin-top:28px;display:flex;gap:10px}
.coach{width:250px;padding-top:47px;text-align:center}
.portrait{width:250px;height:250px;border-radius:50%;border:5px solid #e6e6e6;background:radial-gradient(circle at 45% 35%,#8a8a8a,#2a2a2a 70%)}
.coach-name{margin-top:14px;font-size:21px;color:var(--ink)}
.coach-role{font-size:13.5px;color:var(--accent)}

/* Method */
.method{height:305px;display:flex}
.method-how{width:652px;background:var(--panel);padding:30px 40px 0 191px}
.method-how h2{font-size:31px;font-weight:400;line-height:40px;text-transform:uppercase;color:#2b2b2b}
.method-how h2 span{color:var(--accent)}
.method-how p{margin-top:16px;font-size:11.3px;line-height:24px;color:var(--muted)}
.method-how p a{color:var(--accent);font-weight:600;margin-left:10px}
.method-now{flex:1;padding:34px 0 0 32px;color:var(--white);background:linear-gradient(90deg,#2894cf 0%,#3aa5dc 55%,#7cc2e6 100%)}
.method-now h2{font-size:27px;font-weight:300;line-height:38px;text-transform:uppercase}
.checklist{margin-top:18px;list-style:none;font-size:12.5px}
.checklist li{display:flex;gap:14px;line-height:18px;margin-bottom:11px}
.checklist svg{flex:none;margin-top:3px}

/* Testimonials */
.testimonials{height:395px;text-align:center;position:relative}
.testimonials h2{padding-top:24px;font-size:20.5px;font-weight:600;color:var(--accent);letter-spacing:.3px}
.testimonials .intro{margin:8px auto 0;width:590px;font-size:13px;line-height:18px;color:var(--muted)}
.faces{margin-top:36px;display:flex;justify-content:center;gap:14px}
.face{width:66px;height:64px;border:4px solid #fff;box-shadow:0 0 0 1px #ddd}
.face.a{background:linear-gradient(160deg,#7fa4b8,#b08a6e)}
.face.b{background:linear-gradient(160deg,#3b3b3b,#a07e66);box-shadow:0 0 0 2px #bbb}
.face.c{background:linear-gradient(160deg,#e6e6e6,#c9a48a)}
.quote-box{position:absolute;left:234px;top:217px;width:733px;height:144px;background:var(--accent);border:1px solid #1d88c0;border-radius:3px;color:var(--white);padding:22px 40px 0 56px}
.quote-box::before{content:"";position:absolute;left:355px;top:-14px;border:14px solid transparent;border-top:0;border-bottom-color:var(--accent)}
.quote-mark{position:absolute;left:16px;top:6px;font-size:48px;font-family:Georgia,serif;line-height:1}
.quote-box p{font-size:10.8px;line-height:18px}
.quote-box cite{display:block;margin-top:8px;font-style:normal;font-size:12px}

/* Systems */
.systems{height:460px;display:flex}
.features{width:537px;background:var(--panel);padding:14px 40px 0 191px}
.features p{font-size:11.3px;line-height:25px;color:var(--muted)}
.features h3{margin-top:12px;font-size:18px;font-weight:400;color:var(--accent);line-height:24px}
.features h3 + p{font-size:10.8px;line-height:20px}
.features .more{display:inline-block;margin-top:14px;font-size:14px;color:var(--accent);text-decoration:underline}
.five{flex:1;background:var(--slate);padding:12px 0 0 28px;color:var(--white)}
.five h2{font-size:27px;font-weight:400;line-height:32px;text-transform:uppercase}
.five .tagline{font-size:22px;font-weight:300;color:var(--accent-light);line-height:30px}
.system-grid{margin-top:20px;display:grid;grid-template-columns:235px 200px;row-gap:22px}
.system h3{display:flex;align-items:center;gap:8px;font-size:16.5px;font-weight:400}
.icon{width:32px;height:32px;border-radius:50%;background:#cfd8de;border:2px solid #eef2f4}
.system p{margin-top:6px;font-size:11px;line-height:18px;font-weight:600;width:200px}
.system p a{color:var(--accent-light);font-weight:400;margin-left:6px}

/* Footer */
.touch{height:51px;position:relative}
.touch a{position:absolute;left:503px;top:34px;width:194px;height:42px;background:var(--accent);color:var(--white);font-size:14.5px;display:flex;align-items:center;justify-content:center;letter-spacing:.5px;z-index:2}
.site-footer{height:203px;background:var(--navy);color:#dbe5ec}
.site-footer .wrap{padding-top:58px;display:flex}
.links{list-style:none;font-size:11px;width:140px}
.links li{line-height:20px;display:flex;align-items:center;gap:10px}
.links li::before{content:"";width:0;height:0;border-left:4px solid transparent;border-right:4px solid transparent;border-bottom:6px solid var(--accent)}
.footer-about{width:320px;margin-left:25px;margin-top:-6px}
.footer-about h4{font-size:14px;font-weight:400;color:var(--accent-light)}
.footer-about h4 b{color:var(--white);font-weight:400}
.footer-about p{margin-top:8px;font-size:10.5px;line-height:18px}
.footer-about p a{color:var(--accent-light);margin-left:6px}
.footer-brand{margin-left:18px;margin-top:-4px}
.footer-brand .brand{font-size:21px}
.follow{margin-top:20px;font-size:13px;font-weight:600;color:var(--white)}
.socials{margin-top:8px;display:flex;gap:5px}
.socials span{width:17px;height:17px;border-radius:50%;background:var(--accent)}
.copyright{height:34px;background:var(--navy-deep);color:#dbe5ec;font-size:11px;display:flex;align-items:center;justify-content:center}
</style>
</head>
<body>

<header class="site-header">
  <div class="wrap topbar">
    <span>Call Us : <strong>510-555-0182</strong></span>
    <span>Have an account? or <a class="signin" href="#">Sign In</a></span>
  </div>
  <div class="wrap mainbar">
    <a class="brand" href="#"><span class="brand-mark"></span>Marlowe School of Voice</a>
    <nav class="main-nav">
      <a href="#">Home</a><a href="#">Voice Lessions</a><a href="#">Blog</a><a href="#">What Students Say</a><a href="#">Meet the Instructors</a><a href="#">Voice Ascent</a>
    </nav>
  </div>
</header>

<section class="hero" role="img" aria-label="Blue-toned photograph of piano keys behind the hero">
  <h1 class="hero-title">Voice Ascent</h1>
  <p class="hero-sub">The most technically advanced Platform for singers</p>
  <div class="video-panel">
    <div class="video-frame" role="img" aria-label="Video still of the voice coach">
      <svg class="play" width="62" height="62" viewBox="0 0 62 62" aria-hidden="true">
        <circle cx="31" cy="31" r="29" fill="#2a9fd6" stroke="#e9f6fd" stroke-width="3"/>
        <path d="M25 19 L37 31 L25 43" fill="none" stroke="#0f2535" stroke-width="6" stroke-linecap="round" stroke-linejoin="round"/>
      </svg>
      <div class="video-caption">Evan Daniel Marlowe</div>
    </div>
    <div class="video-copy">
      <p class="lead">Many voice teachers promise ti help your singing.<br>The voice Ascent program is uniquely positioned to transform the way your voice works.</p>
      <p class="body">Vestibulum sed massa a lorem molestie dapibus nec sed magna. Nullam lobortis lectus ut felis viverra elementum. Pellentesque habitant morbi tristique senectus et netus et malesuada fames ac turpis egestas. Nunc viverra libero at pharetra congue. Suspendisse potenti. Nam suscipit blandit est, eget condimentum lorem mattis sed.</p>
      <div class="cta-line">You want to take the admission click on
        <a class="btn btn-blue" href="#">
          <svg width="16" height="14" viewBox="0 0 16 14" aria-hidden="true"><path d="M1 1h3l2 8h8l1-6H5" fill="none" stroke="#fff" stroke-width="1.5"/><circle cx="7" cy="12" r="1.3" fill="#fff"/><circle cx="13" cy="12" r="1.3" fill="#fff"/></svg>
          Add to Cart</a>
      </div>
    </div>
  </div>
</section>

<section class="about">
  <div class="wrap">
    <div class="about-text">
      <h2>About Marlowe School of Voice</h2>
      <p class="lead">Hi, I'm Evan Marlowe, the designer of Voice Ascent, and a professtional voice coach based in the San Francisco Bay Area.</p>
      <p class="body">Phasellus vehicula vehicula sapien, ac tristique enim porta ac. Etiam risus ipsum, tincidunt non dapibus id, congue in nisl. Nunc consectetur gravida erat, aliquam congue augue ullamcorper sit amet. Aenean massa enim, suscipit eu elit vitae, commodo ultricies eros. Suspendisse ultrices feugiat nisl in rhoncus. Etiam mattis lacinia tellus, vel aliquam mauris rhoncus eget.</p>
      <p class="body">Quisque pharetra mattis enim, a tristique mi luctus quis. Etiam ac semper urna. Sed fringilla, ligula quis vulputate feugiat, justo tellus egestas nisl, sed lobortis eros libero non nibh. Praesent ut metus venenatis, sagittis diam vel, consectetur eros.</p>
      <div class="actions">
        <a class="btn btn-grey" href="#">Read More</a>
        <a class="btn btn-blue" href="#">Book Now our Package</a>
      </div>
    </div>
    <div class="coach">
      <div class="portrait" role="img" aria-label="Black and white portrait of the voice coach"></div>
      <p class="coach-name">Evan Marlowe</p>
      <p class="coach-role">Professtional voice coach</p>
    </div>
  </div>
</section>

<section class="method">
  <div class="method-how">
    <h2>How Voice<br><span>Transformation</span> Works</h2>
    <p>After many years of work, I've decided that the effective transformation of the human voice is my life's work and passion.  While on line methods of instruction are not as effective as in person lessons, I find that getting a foundational understanding of the voice that comes with Voice Ascent can greatly enhance your singing voice, whether you're currently studying with a teacher or working on your own. <a href="#">Read More...</a></p>
  </div>
  <div class="method-now" role="img" aria-label="Blue-tinted photograph of a smiling singer">
    <h2>Voice Ascent<br>Available Now</h2>
    <ul class="checklist">
      <li><svg width="11" height="9" viewBox="0 0 11 9"><path d="M1 4.5l3 3 6-6" fill="none" stroke="#fff" stroke-width="2"/></svg>Get Instant Access</li>
      <li><svg width="11" height="9" viewBox="0 0 11 9"><path d="M1 4.5l3 3 6-6" fill="none" stroke="#fff" stroke-width="2"/></svg>Unique methods that are ideal for voice health</li>
      <li><svg width="11" height="9" viewBox="0 0 11 9"><path d="M1 4.5l3 3 6-6" fill="none" stroke="#fff" stroke-width="2"/></svg>The Most Advanced Platform for On Line Singing<br>Instruction</li>
      <li><svg width="11" height="9" viewBox="0 0 11 9"><path d="M1 4.5l3 3 6-6" fill="none" stroke="#fff" stroke-width="2"/></svg>60+ Videos and Audio Workouts</li>
    </ul>
  </div>
</section>

<section class="testimonials">
  <h2>PEOPLE LOVE US. AND SO WILL YOU</h2>
  <p class="intro">Sed ut perspiciatis unde omnis iste natus error sit voluptatem accusantium doloremque laudantium, totam rem aperiam, eaque ipsa quae ab illo inventore.</p>
  <div class="faces">
    <div class="face a" role="img" aria-label="Student photo"></div>
    <div class="face b" role="img" aria-label="Student photo"></div>
    <div class="face c" role="img" aria-label="Student photo"></div>
  </div>
  <blockquote class="quote-box">
    <span class="quote-mark">&ldquo;</span>
    <p>Sed ut perspiciatis unde omnis iste natus error sit voluptatem accusantium doloremque laudantium, totam rem aperiam, eaque ipsa quae ab illo inventore veritatis et quasi architecto beatae vitae dicta sunt explicabo. Nemo enim ipsam voluptatem quia voluptas sit aspernatur aut odit aut fugit, sed quia consequuntur magni dolores eos qui ratione voluptatem sequi nesciunt. Neque porro quisquam est, qui dolorem ipsum quia dolor sit amet, consectetur.</p>
    <cite>Mr. Michael, CEO Lorem Ipsum</cite>
  </blockquote>
</section>

<section class="systems">
  <div class="features">
    <p>Vestibulum sed massa a lorem molestie dapibus nec sed magna. Nullam lobortis lectus ut felis viverra elementum. Pellentesque habitant morbi tristique senectus et netus et malesuada fames ac turpis egestas. Nunc viverra libero at pharetra congue. Suspendisse potenti.</p>
    <h3>Flexibility</h3>
    <p>Vestibulum sed massa a lorem molestie dapibus nec sed magna. Nullam lobortis lectus ut felis viverra elementum.</p>
    <h3>Downloadable Content</h3>
    <p>Vestibulum sed massa a lorem molestie dapibus nec sed magna. Nullam lobortis lectus ut felis viverra elementum.</p>
    <h3>Personal Interaction</h3>
    <p>Vestibulum sed massa a lorem molestie dapibus nec sed magna. Nullam lobortis lectus ut felis viverra elementum.</p>
    <a class="more" href="#">View More...</a>
  </div>
  <div class="five">
    <h2>The Five Systems.</h2>
    <p class="tagline">Five essentials for a strong, free voice.</p>
    <div class="system-grid">
      <div class="system"><h3><span class="icon"></span>Vocal Cords</h3><p>Lorem ipsum dolor sit amet, consec tetur adipiscing elitv estibulum soll icitudin.<a href="#">Read More...</a></p></div>
      <div class="system"><h3><span class="icon"></span>Air Control</h3><p>Lorem ipsum dolor sit amet, consec tetur adipiscing elitv estibulum soll icitudin.<a href="#">Read More...</a></p></div>
      <div class="system"><h3><span class="icon"></span>Outer Muscles</h3><p>Lorem ipsum dolor sit amet, consec tetur adipiscing elitv estibulum soll icitudin.<a href="#">Read More...</a></p></div>
      <div class="system"><h3><span class="icon"></span>Pharynx</h3><p>Lorem ipsum dolor sit amet, consec tetur adipiscing elitv estibulum soll icitudin.<a href="#">Read More...</a></p></div>
      <div class="system"><h3><span class="icon"></span>Outer Muscles</h3><p>Lorem ipsum dolor sit amet, consec tetur adipiscing elitv estibulum soll icitudin.<a href="#">Read More...</a></p></div>
    </div>
  </div>
</section>

<div class="touch"><a href="#">GET IN TOUCH</a></div>

<footer class="site-footer">
  <div class="wrap">
    <ul class="links">
      <li>About us</li><li>Support</li><li>EDM Method</li><li>Privacy Policy</li><li>Terms of use</li><li>Sitemap</li>
    </ul>
    <ul class="links">
      <li>Home</li><li>Voice Lessions</li><li>Blog</li><li>What Students Say</li><li>Meet the Instructors</li><li>Voice Ascent</li>
    </ul>
    <div class="footer-about">
      <h4>About <b>Marlowe</b> School of Voice</h4>
      <p>Lorem ipsum dolor sit amet, consectetur adipiscing elit. Maecenas vehicula imperdiet sapien at consequat. Nam ullamcorper sollicitudin nisi feugiat facilisis. Interdum et malesuada fames ac ante ipsum primis in faucibus. Pellentesque mi ipsum, bibendum.<a href="#">Read More...</a></p>
    </div>
    <div class="footer-brand">
      <a class="brand" href="#"><span class="brand-mark"></span>Marlowe</a>
      <p class="follow">Follow Us</p>
      <div class="socials"><span></span><span></span><span></span><span></span></div>
    </div>
  </div>
</footer>
<div class="copyright">© Copyright 2013, plorvetune.com</div>

</body>
</html>
```